I need a Canva design for my company for real estate new listings

A new listing Canva template for properties we list, also a sold and under contract template. We are an outdoor brand thornbrookestates.com so it needs to flow with our designs.

```html
<!DOCTYPE html>
<html lang="en">
<head>
<meta charset="utf-8">
<title>Thornbrook Estates – Listing Templates</title>
<link href="https://fonts.googleapis.com/css2?family=Oswald:wght@600;700&family=Montserrat:wght@500;600;700&display=swap" rel="stylesheet">
<style>
  :root{
    --paper:#f4f1ec;
    --board:#efebe5;
    --brown:#5b3412;
    --brown-dark:#4a2a10;
    --ink:#3c2512;
    --white:#ffffff;
    --sky:#c9d6e2;
    --forest:#3f4a2c;
    --meadow:#a27a3a;
    --sunset:#d58a3a;
  }
  *{margin:0;padding:0;box-sizing:border-box}
  html,body{width:1200px;height:977px;overflow:hidden;background:var(--board)}
  body{position:relative;font-family:"Montserrat",sans-serif;color:var(--ink)}

  .card{position:absolute;background:var(--paper);border:1px solid #3a3a3a;overflow:hidden}
  .card--listing{left:149px;top:163px;width:515px;height:622px}
  .card--contract{left:704px;top:167px;width:337px;height:306px}
  .card--sold{left:704px;top:487px;width:337px;height:298px}

  .photo{position:absolute;left:0;right:0}
  .card--listing .photo{top:100px;height:373px;
    background:linear-gradient(180deg,rgba(244,241,236,0) 0%,var(--sky) 40%,#8e99a0 58%,var(--forest) 72%,#4d5a33 86%,var(--meadow) 100%)}
  .card--contract .photo{top:136px;height:96px;
    background:linear-gradient(180deg,#b9a88e 0%,#8c6d45 40%,#6b5a2e 65%,var(--meadow) 100%)}
  .card--sold .photo{top:102px;height:120px;
    background:linear-gradient(180deg,#e8cfae 0%,var(--sunset) 30%,#5d5a2e 55%,#2f3a22 100%)}

  .brand{position:absolute;display:flex;align-items:center;gap:6px;font-weight:700;color:var(--brown);white-space:nowrap}
  .brand__dot{border-radius:50%;background:var(--brown)}
  .card--listing .brand{left:22px;top:52px;font-size:17px}
  .card--listing .brand__dot{width:14px;height:14px}
  .card--contract .brand,.card--sold .brand{left:12px;top:38px;font-size:10px;gap:4px}
  .card--contract .brand__dot,.card--sold .brand__dot{width:8px;height:8px}

  .headline{position:absolute;font-family:"Oswald",sans-serif;font-weight:700;color:var(--brown);text-transform:uppercase;line-height:1}
  .card--listing .headline{left:22px;top:130px;letter-spacing:2px}
  .headline__line--sm{font-size:68px;display:block}
  .headline__line--lg{font-size:80px;display:block;margin-top:6px}
  .card--contract .headline{left:140px;top:28px;font-size:40px;line-height:1.02;letter-spacing:1px}
  .card--sold .headline{left:0;right:0;padding-left:140px;top:12px;font-size:62px;text-align:center;padding-right:30px;letter-spacing:2px}

  .tagline{position:absolute;border-top:1.5px solid var(--brown);color:var(--brown);white-space:nowrap}
  .card--listing .tagline{left:22px;top:285px;width:262px;padding-top:4px;font-size:15.5px;font-weight:600;background:var(--paper);padding-left:1px}
  .card--contract .tagline{left:140px;top:113px;width:173px;padding-top:5px;font-size:8.5px;font-weight:600;letter-spacing:1.6px}
  .card--sold .tagline{left:142px;top:80px;width:172px;padding-top:5px;font-size:8.5px;font-weight:600;letter-spacing:1.6px}

  .info-band{position:absolute;left:0;right:0;background:var(--brown);color:var(--white);font-weight:600;text-align:center;display:flex;align-items:center;justify-content:center}
  .card--listing .info-band{top:473px;height:93px;font-size:17.5px;line-height:1.45}
  .card--contract .info-band{top:232px;height:48px;font-size:10px;line-height:1.5}
  .card--sold .info-band{top:222px;height:48px;font-size:10px;line-height:1.5}

  .site{position:absolute;left:0;right:0;display:flex;align-items:center;justify-content:center;gap:6px;font-weight:600;text-transform:uppercase;color:var(--ink)}
  .card--listing .site{top:585px;font-size:12px;letter-spacing:2.6px}
  .card--contract .site{top:285px;font-size:7.5px;letter-spacing:1.4px;gap:4px}
  .card--sold .site{top:280px;font-size:7.5px;letter-spacing:1.4px;gap:4px}
  .site svg{flex:none}
</style>
</head>
<body>

<section class="card card--listing">
  <div class="photo" role="img" aria-label="Mountain valley with pine forest, meadow and a small lake under a cloudy sky"></div>
  <div class="brand"><span class="brand__dot"></span>Thornbrook Estates</div>
  <h1 class="headline"><span class="headline__line--sm">New</span><span class="headline__line--lg">Listing</span></h1>
  <p class="tagline">SELLING LAND THE RIGHT WAY</p>
  <p class="info-band">I think that would be the best place for info on<br>the property. Pitt County, NC 200 Acres $1,000,000</p>
  <p class="site"><svg width="14" height="14" viewBox="0 0 14 14" fill="none" stroke="currentColor" stroke-width="1"><circle cx="7" cy="7" r="6"/><ellipse cx="7" cy="7" rx="2.6" ry="6"/><path d="M1 7h12M2 4h10M2 10h10"/></svg>thornbrookestates.com</p>
</section>

<section class="card card--contract">
  <div class="photo" role="img" aria-label="Golden hillside meadow with pine trees and distant mountains"></div>
  <div class="brand"><span class="brand__dot"></span>Thornbrook Estates</div>
  <h2 class="headline">Under<br>Contract</h2>
  <p class="tagline">GREAT LAND. GREAT FUTURE.</p>
  <p class="info-band">I think that would be the best place for info on<br>the property. Pitt County, NC 200 Acres $1,000,000</p>
  <p class="site"><svg width="8" height="8" viewBox="0 0 14 14" fill="none" stroke="currentColor" stroke-width="1.4"><circle cx="7" cy="7" r="6"/><ellipse cx="7" cy="7" rx="2.6" ry="6"/><path d="M1 7h12"/></svg>thornbrookestates.com</p>
</section>

<section class="card card--sold">
  <div class="photo" role="img" aria-label="Sunset over a forested river valley"></div>
  <div class="brand"><span class="brand__dot"></span>Thornbrook Estates</div>
  <h2 class="headline">Sold</h2>
  <p class="tagline">ANOTHER LEGACY SECURED.</p>
  <p class="info-band">I think that would be the best place for info on<br>the property. Pitt County, NC 200 Acres $1,000,000</p>
  <p class="site"><svg width="8" height="8" viewBox="0 0 14 14" fill="none" stroke="currentColor" stroke-width="1.4"><circle cx="7" cy="7" r="6"/><ellipse cx="7" cy="7" rx="2.6" ry="6"/><path d="M1 7h12"/></svg>thornbrookestates.com</p>
</section>

</body>
</html>
```